Custom Home Builder Needs a Website

Harbor Stone Builders Ltd. requires a clean professional 5 page website - Home, About Us, Gallery (Interior and Exterior), Our Process and Contact Us(with registration form). We are a home builder who also has homes for sale. Also please have a place for video embedding. Editable fields by user. Using the stationery 'feel' that is attached. Need social media links. If you require any additional files, please request.

Target Market(s)

Families and professionals

Industry/Entity Type

Home Builder

Coding

Coded - Design and coding required

Number of Pages Required

5+ page

Font styles to use
Sans Serif
Other font styles liked:
• Lato

Requirements
Must have
• Editable by user
• Register Button
• Place to put home models for sale - preferably on the first page
• 5 page website -
• -Home
• -About Us
• -Gallery (Interior and Exterior)
• -Our Process
• -Contact Us.
Nice to have
• Themed similar to current stationery
• place for video embedding
• Try some darker backgrounds
• Change pictures to B/W if works for design
Should not have
• cartoonish type of content

```html
<!DOCTYPE html>
<html lang="en">
<head>
<meta charset="utf-8">
<title>Harbor Stone Builders Ltd.</title>
<link href="https://fonts.googleapis.com/css2?family=Lato:wght@400;700&family=Roboto:wght@400;500&display=swap" rel="stylesheet">
<style>
:root{
  --black:#050505;
  --green:#4ea346;
  --green-dark:#3f8f38;
  --lime:#a2c523;
  --grey-bg:#f4f5f7;
  --text:#7a7a7a;
  --heading:#666;
  --footer:#1d1d1d;
  --white:#fff;
}
*{box-sizing:border-box;margin:0;padding:0}
html,body{width:1200px;height:2528px;overflow:hidden}
body{position:relative;background:var(--white);font-family:Arial,Helvetica,sans-serif;color:var(--text)}
.abs{position:absolute}
.site-header{left:0;top:0;width:1200px;height:101px;background:var(--black);border-top:3px solid var(--green)}
.brand{left:88px;top:26px;width:220px;color:var(--green);font-family:Lato,sans-serif;font-weight:700;font-size:22px;line-height:24px;letter-spacing:.5px}
.call{left:866px;top:22px;display:flex;align-items:center;gap:14px;color:var(--green);font-family:Roboto,sans-serif;font-size:18px}
.call-ring{width:50px;height:50px;border:2px solid var(--green);border-radius:50%;display:flex;align-items:center;justify-content:center}
.main-nav{left:0;top:101px;width:1200px;height:56px;background:linear-gradient(#5cb450,var(--green-dark))}
.nav-item{top:0;height:56px;line-height:56px;color:var(--white);font-family:Lato,sans-serif;font-size:13px;text-align:center;width:0;display:flex;justify-content:center;white-space:nowrap}
.nav-sep{top:0;width:1px;height:56px;background:rgba(255,255,255,.25)}
.search{left:834px;top:113px;width:261px;height:31px;background:var(--white);border-radius:2px;font-size:12px;color:#777;padding:9px 14px;font-family:Roboto,sans-serif}
.search svg{position:absolute;right:12px;top:9px}
.hero{left:0;top:157px;width:1200px;height:502px;background:linear-gradient(100deg,#3c3935 0%,#8c8377 30%,#c7c2b8 55%,#9c8f7e 75%,#6d6459 100%)}
.hero-caption{left:88px;top:323px;width:434px;height:220px;background:rgba(20,20,20,.72);padding:22px 22px}
.hero-caption h1{color:var(--lime);font-family:Lato,sans-serif;font-weight:700;font-size:27px;line-height:40px;white-space:nowrap}
.hero-caption p{color:var(--white);font-size:12px;line-height:25px;margin-top:10px}
.btn-outline{display:inline-block;margin-top:14px;border:1px solid var(--lime);color:var(--white);font-family:Lato,sans-serif;font-weight:700;font-size:13px;padding:8px 10px;border-radius:2px}
.dots{left:458px;top:510px;display:flex;gap:5px}
.dots i{width:8px;height:8px;border-radius:50%;background:var(--lime)}
.video{left:86px;top:720px;width:527px;height:331px;background:linear-gradient(#8aa0b4 0%,#6f7469 40%,#3f3d39 70%,#6d8a3a 100%)}
.play{left:322px;top:858px;width:56px;height:56px;border-radius:50%;background:rgba(0,0,0,.55);border:2px solid var(--white)}
.welcome{left:662px;top:716px;width:420px}
.welcome h2{font-family:Lato,sans-serif;font-weight:400;font-size:21px;color:var(--heading)}
.welcome h3{font-family:Lato,sans-serif;font-weight:700;font-size:27px;color:var(--lime);margin-top:4px;white-space:nowrap}
.welcome p{font-size:12.5px;line-height:26px;margin-top:14px}
.read-more{display:inline-flex;align-items:center;gap:6px;margin-top:20px;color:var(--lime);font-family:Lato,sans-serif;font-size:13px;text-decoration:underline}
.process{left:0;top:1104px;width:1200px;height:401px;background:var(--grey-bg)}
.section-title{left:0;width:1200px;text-align:center;font-family:Lato,sans-serif;font-weight:700;font-size:25px;color:var(--heading)}
.section-title span{color:var(--lime)}
.section-sub{left:0;width:1200px;text-align:center;font-size:12.5px}
.step{top:1237px;width:300px;text-align:center}
.step-icon{margin:0 auto;width:110px;height:110px;border-radius:50%;border:4px solid var(--green);display:flex;align-items:center;justify-content:center}
.step-icon div{width:94px;height:94px;border-radius:50%;background:var(--lime);display:flex;align-items:center;justify-content:center}
.step h4{font-family:Roboto,sans-serif;font-weight:400;font-size:20px;color:var(--green);margin-top:18px}
.step p{font-size:12px;line-height:25px;margin-top:10px;padding:0 20px}
.photo{background:linear-gradient(#a7a8a2,#54524d)}
.partners{left:0;top:2103px;width:1200px;height:115px;background:var(--green)}
.partner{top:2123px;width:145px;height:76px;border:1px solid rgba(255,255,255,.45);display:flex;align-items:center;justify-content:center}
.partner i{width:70px;height:22px;border-radius:3px;background:rgba(255,255,255,.85)}
.site-footer{left:0;top:2218px;width:1200px;height:310px;background:var(--footer);color:var(--white)}
.foot-brand{left:88px;top:2320px;width:260px;color:var(--green);font-family:Lato,sans-serif;font-weight:700;font-size:26px;line-height:30px}
.foot-h{top:2256px;font-family:Lato,sans-serif;font-weight:700;font-size:17px;color:var(--white)}
.contact-line{left:388px;display:flex;align-items:center;gap:14px;font-size:11.5px;color:var(--white)}
.contact-line svg{width:14px;height:14px}
.news-text{left:635px;top:2298px;width:220px;font-size:12px;line-height:20px;color:var(--white)}
.news-input{left:635px;top:2354px;width:209px;height:34px;background:var(--white);color:#666;font-size:12px;padding:10px 12px}
.subscribe{left:635px;top:2401px;background:var(--lime);color:var(--white);font-size:10px;padding:7px 10px}
.follow-text{left:897px;top:2300px;width:210px;font-size:11.5px;line-height:19px;color:var(--white)}
.social{top:2376px;width:36px;height:36px;border-radius:50%;border:2px solid var(--white)}
.divider{left:88px;top:2457px;width:1024px;height:1px;background:#333}
.copyright{left:0;top:2483px;width:1200px;text-align:center;font-size:12px;color:var(--white)}
</style>
</head>
<body>
<header class="abs site-header"></header>
<div class="abs brand">HARBOR STONE BUILDERS</div>
<div class="abs call">
  <div class="call-ring"><svg width="18" height="18" viewBox="0 0 24 24"><path fill="#4ea346" d="M6.6 10.8a15 15 0 0 0 6.6 6.6l2.2-2.2c.3-.3.7-.4 1-.2 1.1.4 2.3.6 3.6.6.6 0 1 .4 1 1V20c0 .6-.4 1-1 1A17 17 0 0 1 3 4c0-.6.4-1 1-1h3.5c.6 0 1 .4 1 1 0 1.3.2 2.5.6 3.6.1.3 0 .7-.2 1z"/></svg></div>
  <span>CALL US : 306-555-2140</span>
</div>

<nav class="abs main-nav"></nav>
<div class="abs nav-item" style="left:158px;top:101px">HOME</div>
<div class="abs nav-sep" style="left:224px;top:101px"></div>
<div class="abs nav-item" style="left:290px;top:101px">ABOUT US</div>
<div class="abs nav-sep" style="left:358px;top:101px"></div>
<div class="abs nav-item" style="left:430px;top:101px">GALLERY</div>
<div class="abs nav-sep" style="left:500px;top:101px"></div>
<div class="abs nav-item" style="left:581px;top:101px">OUR PROCESS</div>
<div class="abs nav-sep" style="left:666px;top:101px"></div>
<div class="abs nav-item" style="left:745px;top:101px">CONTACT US</div>
<div class="abs nav-sep" style="left:820px;top:101px"></div>
<div class="abs search">SEARCH<svg width="12" height="12" viewBox="0 0 12 12"><circle cx="5" cy="5" r="3.6" fill="none" stroke="#777" stroke-width="1.4"/><path d="M7.7 7.7 11 11" stroke="#777" stroke-width="1.4"/></svg></div>

<div class="abs hero" role="img" aria-label="Photo of a bright master bathroom with double vanity and glass shower"></div>
<div class="abs hero-caption">
  <h1>HARBOR STONE BUILDERS</h1>
  <p>Sed ut perspiciatis unde omnis iste natus error sit voluptatem accusantium doloremque laudantium, totam rem aperiam, eaque ipsa quae ab illo invent ore veritatis et quasi architecto beatae vitae</p>
  <span class="btn-outline">READ MORE</span>
</div>
<div class="abs dots"><i></i><i></i><i></i></div>

<div class="abs video" role="img" aria-label="Video still of a newly built two-storey home with landscaped front yard"></div>
<div class="abs play"><svg width="52" height="52" viewBox="0 0 52 52"><path d="M21 16v20l15-10z" fill="#fff"/></svg></div>
<section class="abs welcome">
  <h2>WELCOME TO</h2>
  <h3>HARBOR STONE BUILDERS</h3>
  <p>Sed ut perspiciatis unde omnis iste natus error sit voluptatem accusantium doloremque laudantium, totam rem aperiam, eaque ipsa quae ab illo invent ore veritatis et quasi architecto beatae vitae dicta sunt explicabo. Nemo enim ipsam voluptatem quia voluptas sit aspernatur aut odit aut fugit, sed quia eos qui ratione voluptatem sequi nesciunt.</p>
  <p>Aperiam, eaque ipsa quae ab illo invent ore veritatis et quasi architecto beat ae vitae dicta sunt explicabo. Nemo enim ipsam voluptatem quia voluptas sit eos qui ratione voluptatem sequi nesciunt.</p>
  <span class="read-more">Read More Info <svg width="13" height="13" viewBox="0 0 14 14"><circle cx="7" cy="7" r="6" fill="none" stroke="#a2c523" stroke-width="1.4"/><path d="M6 4.5 8.5 7 6 9.5" fill="none" stroke="#a2c523" stroke-width="1.4"/></svg></span>
</section>

<section class="abs process"></section>
<h2 class="abs section-title" style="top:1135px">OUR <span>PROCESS</span></h2>
<p class="abs section-sub" style="top:1180px">Sed ut perspiciatis unde omnis iste natus error sit voluptatem accusantium doloremque laudantium</p>
<div class="abs step" style="left:96px">
  <div class="step-icon"><div><svg width="46" height="46" viewBox="0 0 46 46" fill="none" stroke="#fff" stroke-width="3"><path d="M10 36 34 12l4 4-24 24H10z"/><path d="M8 14l6-6 24 24-6 6z" opacity=".8"/></svg></div></div>
  <h4>Custom</h4>
  <p>Sed ut perspiciatis unde omnis iste natus error sit voluptatem accusantium doloremque vitae dicta sunt explicabo.</p>
</div>
<div class="abs step" style="left:448px">
  <div class="step-icon"><div><svg width="46" height="46" viewBox="0 0 46 46" fill="#fff"><path d="M11 20a12 12 0 0 1 24 0h3v4H8v-4z"/><rect x="19" y="8" width="8" height="8" rx="1"/><path d="M10 42c0-7 6-12 13-12s13 5 13 12z"/></svg></div></div>
  <h4>Builder</h4>
  <p>Sed ut perspiciatis unde omnis iste natus error sit voluptatem accusantium doloremque vitae dicta sunt explicabo.</p>
</div>
<div class="abs step" style="left:800px">
  <div class="step-icon"><div><svg width="46" height="46" viewBox="0 0 46 46" fill="none" stroke="#fff" stroke-width="3"><path d="M24 6h14v14L20 38 6 24z"/><circle cx="31" cy="13" r="2.5"/></svg></div></div>
  <h4>Sale</h4>
  <p>Sed ut perspiciatis unde omnis iste natus error sit voluptatem accusantium doloremque vitae dicta sunt explicabo.</p>
</div>

<h2 class="abs section-title" style="top:1535px">PHOTO <span>GALLERY</span></h2>
<p class="abs section-sub" style="top:1580px">Sed ut perspiciatis unde omnis iste natus error sit voluptatem accusantium doloremque laudantium</p>
<div class="abs photo" style="left:86px;top:1626px;width:507px;height:207px;background:linear-gradient(#6f7a6a,#4a4b49 60%,#8a8780)" role="img" aria-label="Exterior of a grey craftsman home with triple garage"></div>
<div class="abs photo" style="left:607px;top:1626px;width:247px;height:430px;background:linear-gradient(#d9dbdc,#5a5d5b 45%,#6e6c65)" role="img" aria-label="Front of a two-storey home with stone accents"></div>
<div class="abs photo" style="left:866px;top:1626px;width:248px;height:207px;background:linear-gradient(#d8d2c4,#a89c86 50%,#efeee9)" role="img" aria-label="Kitchen with white cabinets and granite counters"></div>
<div class="abs photo" style="left:86px;top:1848px;width:248px;height:208px;background:linear-gradient(#b3aa9c,#6d6962 60%,#2f2d2b)" role="img" aria-label="Kitchen backsplash and range detail"></div>
<div class="abs photo" style="left:345px;top:1848px;width:248px;height:208px;background:linear-gradient(#e3e5e6,#6b655d 50%,#8b8578)" role="img" aria-label="Bungalow with stone front and attached garage"></div>
<div class="abs photo" style="left:866px;top:1848px;width:248px;height:208px;background:linear-gradient(#e2e4e5,#5a5a55 50%,#7b776f)" role="img" aria-label="Two-storey home with balcony and double garage"></div>

<section class="abs partners"></section>
<div class="abs partner" style="left:86px"><i></i></div>
<div class="abs partner" style="left:263px"><i></i></div>
<div class="abs partner" style="left:440px"><i></i></div>
<div class="abs partner" style="left:617px"><i></i></div>
<div class="abs partner" style="left:794px"><i></i></div>
<div class="abs partner" style="left:971px"><i></i></div>

<footer class="abs site-footer"></footer>
<div class="abs foot-brand">HARBOR STONE BUILDERS LTD.</div>
<h5 class="abs foot-h" style="left:388px">CONTACT US</h5>
<div class="abs contact-line" style="top:2302px"><svg viewBox="0 0 24 24"><path fill="#fff" d="M6.6 10.8a15 15 0 0 0 6.6 6.6l2.2-2.2c.3-.3.7-.4 1-.2 1.1.4 2.3.6 3.6.6.6 0 1 .4 1 1V20c0 .6-.4 1-1 1A17 17 0 0 1 3 4c0-.6.4-1 1-1h3.5c.6 0 1 .4 1 1 0 1.3.2 2.5.6 3.6.1.3 0 .7-.2 1z"/></svg>306-555-2140 (Phone)</div>
<div class="abs contact-line" style="top:2332px"><svg viewBox="0 0 24 24"><rect x="6" y="3" width="12" height="6" fill="#fff"/><rect x="3" y="9" width="18" height="9" rx="2" fill="#fff"/><rect x="7" y="15" width="10" height="6" fill="#fff" stroke="#1d1d1d"/></svg>306-555-2140 (Fax)</div>
<div class="abs contact-line" style="top:2361px"><svg viewBox="0 0 24 24"><rect x="3" y="6" width="18" height="12" fill="none" stroke="#fff" stroke-width="2"/><path d="M3 6l9 7 9-7" fill="none" stroke="#fff" stroke-width="2"/></svg><u>hello@harborstonebuilders.ca</u></div>
<div class="abs contact-line" style="top:2390px"><svg viewBox="0 0 24 24"><path fill="#fff" d="M12 2a7 7 0 0 0-7 7c0 5 7 13 7 13s7-8 7-13a7 7 0 0 0-7-7zm0 9.5A2.5 2.5 0 1 1 12 6.5a2.5 2.5 0 0 1 0 5z"/></svg>PO Box 218 Lakeview, SK S0K 2L0</div>

<h5 class="abs foot-h" style="left:635px">NEWSLETTER</h5>
<p class="abs news-text">Register Your email address to get information ablout us</p>
<div class="abs news-input">Email Address</div>
<div class="abs subscribe">SUBSCRIBE</div>

<h5 class="abs foot-h" style="left:897px">FOLLOW US</h5>
<p class="abs follow-text">Lorem ipsum dolor sit amet, conse ctetur adipiscing elit. Nulla in purus nibh. Donec ornare</p>
<div class="abs social" style="left:893px"></div>
<div class="abs social" style="left:937px"></div>
<div class="abs social" style="left:981px"></div>
<div class="abs social" style="left:1025px"></div>
<div class="abs social" style="left:1069px"></div>

<div class="abs divider"></div>
<p class="abs copyright">© 2016 Copyright&nbsp; Harbor Stone Builders All rights reserved</p>
</body>
</html>
```